Willowmere Counseling (Endure - Mend - Flourish) - Double Sided Business Card

I would like a 2-sided business card. Front: Matte Black or Navy with Logo & Tagline. Back: Name, Address, Phone Number, Email, & Website (maybe would like to include a small map pin-pointing location); Prefer front to be a gold/silver foil (iridescent); Back prefer white or light colored background with lettering that is easy to read and simple

Target Market(s)

Individuals & Couples (13 y.o. - ALL Adults); High end clientele

Industry/Entity Type

Licensed Professional Counselor (Mental Health)

Contact Information for Business Card

Name: Willowmere Counseling; Tagline: Endure - Mend - Flourish; Address: 3870 N. Garrick Ave., Suite 214, Fort Worth, TX 76132; Phone: (214) 555-0187; Website: www.WillowmereCounseling.example

Font styles to use
Serif

Requirements
Must have
• Logo on Front (Large) prefer gold/silver foil on a matte dark color (i.e. black, navy, etc.); Back of Card: All other relevant information

```html
<!DOCTYPE html>
<html lang="en">
<head>
<meta charset="utf-8">
<title>Willowmere Counseling – Business Card</title>
<link href="https://fonts.googleapis.com/css2?family=Cinzel:wght@400;600&family=Roboto:wght@400;700&display=swap" rel="stylesheet">
<style>
  :root {
    --backdrop: #3a3a3a;
    --card-dark: #161616;
    --card-light: #f5f2ea;
    --card-edge: #c9a53a;
    --gold: #d9b43e;
    --gold-deep: #a9862a;
    --silver: #a7a7a7;
    --ink: #222222;
    --ink-soft: #6a6a6a;
  }
  * { box-sizing: border-box; margin: 0; padding: 0; }
  html, body { width: 1200px; height: 801px; overflow: hidden; }
  body { background: var(--backdrop); position: relative; font-family: "Roboto", Arial, sans-serif; }

  .card {
    position: absolute;
    top: 249px;
    width: 530px;
    height: 303px;
    box-shadow: 0 0 0 1.5px var(--card-edge), 0 12px 30px rgba(0,0,0,.45);
    border-radius: 2px;
    overflow: hidden;
  }
  .card--front { left: 40px; background: var(--card-dark); }
  .card--back { left: 630px; background: var(--card-light); }

  /* Front: name and tagline */
  .brand {
    position: absolute; inset: 0;
    display: flex; flex-direction: column; justify-content: center; align-items: center;
    text-align: center;
  }
  .brand__dot {
    width: 44px; height: 44px; border-radius: 50%;
    background: var(--gold);
    margin-bottom: 18px;
  }
  .brand__name {
    font-family: "Cinzel", Georgia, serif;
    font-weight: 600;
    font-size: 34px;
    line-height: 1.15;
    color: var(--gold);
    letter-spacing: 1.5px;
  }
  .brand__rule { width: 260px; height: 1px; background: var(--silver); margin: 14px 0 10px; }
  .brand__tagline {
    font-family: "Cinzel", Georgia, serif;
    font-size: 13px;
    color: var(--gold);
    letter-spacing: 2px;
  }

  /* Back: contact details */
  .contact {
    position: absolute;
    left: 48px; top: 52px; right: 40px;
    color: var(--ink);
    font-size: 14px;
    line-height: 1.5;
  }
  .contact__firm {
    font-family: "Cinzel", Georgia, serif;
    font-weight: 600;
    font-size: 15px;
    color: var(--gold-deep);
    letter-spacing: 1px;
    margin-bottom: 14px;
  }
  .contact__name { font-weight: 700; font-size: 19px; letter-spacing: .3px; color: var(--ink); }
  .contact__title { color: var(--ink-soft); font-size: 13.5px; margin-bottom: 10px; }
  .contact__rule { width: 60px; height: 2px; background: var(--gold); margin-bottom: 12px; }
  .contact__address { margin-bottom: 10px; }
  .contact__list { list-style: none; }
  .contact__list li { display: flex; align-items: center; gap: 9px; }
  .contact__list svg { width: 13px; height: 13px; flex: none; }
</style>
</head>
<body>

<section class="card card--front">
  <div class="brand">
    <div class="brand__dot"></div>
    <p class="brand__name">Willowmere<br>Counseling</p>
    <div class="brand__rule"></div>
    <p class="brand__tagline">Endure - Mend - Flourish</p>
  </div>
</section>

<section class="card card--back">
  <div class="contact">
    <p class="contact__firm">Willowmere Counseling</p>
    <p class="contact__name">DANIEL HARTWELL</p>
    <p class="contact__title">President</p>
    <div class="contact__rule"></div>
    <p class="contact__address">3870 N. Garrick Ave., Suite 214<br>Fort Worth, TX 76132</p>
    <ul class="contact__list">
      <li>
        <svg viewBox="0 0 24 24" aria-hidden="true"><path fill="#a9862a" d="M6.6 10.8a15.1 15.1 0 0 0 6.6 6.6l2.2-2.2a1 1 0 0 1 1-.25 11.4 11.4 0 0 0 3.6.57 1 1 0 0 1 1 1V20a1 1 0 0 1-1 1A17 17 0 0 1 3 4a1 1 0 0 1 1-1h3.5a1 1 0 0 1 1 1c0 1.25.2 2.45.57 3.57a1 1 0 0 1-.25 1z"/></svg>
        (214) 555-0187
      </li>
      <li>
        <svg viewBox="0 0 24 24" aria-hidden="true"><path d="M2 5h20v14H2z M2 5l10 8 10-8" fill="none" stroke="#a9862a" stroke-width="2.4"/></svg>
        info@WillowmereCounseling.example
      </li>
      <li>
        <svg viewBox="0 0 24 24" aria-hidden="true"><circle cx="12" cy="12" r="9.5" fill="none" stroke="#a9862a" stroke-width="2.4"/><path d="M2.5 12h19M12 2.5c3 3 3 16 0 19M12 2.5c-3 3-3 16 0 19" fill="none" stroke="#a9862a" stroke-width="2"/></svg>
        www.WillowmereCounseling.example
      </li>
    </ul>
  </div>
</section>

</body>
</html>
```